Brightvale Fluid Systems Corp Business Cards

Business cards to match the logo.

Company is a start up water technology company that has developed a patented system using centrifugal force to separate waste from municipal waste water to produce crystal clear clean water. Product sell starting at 2 million to governments both in the US and international.

Business cards should have a professional look with the target generally engineers.

Target Market(s)

Engineers, Government officials and investors

Industry/Entity Type

Water Treatment

Contact Information for Business Card

Business cards design will be used for 6 to 8 people with job titles. Can use the quote "If there is magic in the planet, it is contained in water." but not required to use quote. Should follow theme of Logo

Font styles to use
Other font styles liked:
• match logo font

Requirements
Nice to have
• Colors to match Logo. Business cards to match style of flow of Logo.
• Emphasis on clean look not a busy look. Clean flowing water.
Should not have
• Pictures of industrial equipment or wastewater

```html
<!DOCTYPE html>
<html lang="en">
<head>
<meta charset="utf-8">
<title>Brightvale Fluid Systems Business Cards</title>
<link href="https://fonts.googleapis.com/css2?family=Playfair+Display:wght@400&family=Arimo:wght@400;700&display=swap" rel="stylesheet">
<style>
  :root {
    --page-bg: #666666;
    --navy: #0b5079;
    --sky: #2aa9e0;
    --white: #ffffff;
  }
  * { box-sizing: border-box; margin: 0; padding: 0; }
  html, body {
    width: 1200px;
    height: 802px;
    overflow: hidden;
    background: var(--page-bg);
    font-family: "Arimo", Arial, sans-serif;
  }
  .card {
    position: absolute;
    top: 274px;
    width: 443px;
    height: 265px;
    overflow: hidden;
  }
  .card--front { left: 136px; background: var(--navy); }
  .card--back { left: 624px; background: var(--white); }

  .card__stripe {
    position: absolute;
    top: 0;
    bottom: 0;
    left: 378px;
    width: 12px;
    background: var(--white);
  }
  .card__band {
    position: absolute;
    top: 0;
    bottom: 0;
    left: 390px;
    right: 0;
    background: var(--sky);
  }

  .wordmark {
    font-family: "Playfair Display", Georgia, serif;
    font-weight: 400;
    text-transform: uppercase;
    text-align: center;
    line-height: 1.1;
    letter-spacing: 2px;
  }
  .card--front .wordmark {
    position: absolute;
    left: 80px;
    top: 46px;
    width: 260px;
    font-size: 23px;
    color: var(--white);
  }
  .card--back .wordmark {
    position: absolute;
    left: 0;
    top: 90px;
    width: 443px;
    font-size: 31px;
    color: var(--navy);
  }

  .contact {
    position: absolute;
    right: 138px;
    top: 136px;
    text-align: right;
    color: var(--white);
  }
  .contact__name { font-weight: 700; font-size: 16px; letter-spacing: 0.2px; }
  .contact__title { font-size: 12.5px; margin-top: 1px; }
  .contact__list { list-style: none; margin-top: 15px; }
  .contact__item {
    font-size: 12.5px;
    line-height: 16px;
    display: flex;
    justify-content: flex-end;
    align-items: center;
    gap: 4px;
  }
  .contact__icon { width: 11px; height: 11px; flex: none; }

  .tagline {
    position: absolute;
    left: 0;
    bottom: 0;
    width: 443px;
    height: 47px;
    background: var(--navy);
    color: var(--white);
    font-size: 11.5px;
    display: flex;
    align-items: center;
    justify-content: center;
    text-transform: uppercase;
  }
</style>
</head>
<body>
  <section class="card card--front">
    <div class="card__stripe"></div>
    <div class="card__band"></div>
    <div class="wordmark">Brightvale Fluid<br>Systems</div>
    <div class="contact">
      <div class="contact__name">DANIEL HARLOW</div>
      <div class="contact__title">Managing Director</div>
      <ul class="contact__list">
        <li class="contact__item">055-210 348 617
          <svg class="contact__icon" viewBox="0 0 12 12" aria-hidden="true"><path d="M1 4 Q6 0 11 4 L9.5 5.5 L8 4.5 L4 4.5 L2.5 5.5 Z M3 6 L9 6 L10 11 L2 11 Z" fill="var(--white)"/></svg>
        </li>
        <li class="contact__item">055-210 348 618
          <svg class="contact__icon" viewBox="0 0 12 12" aria-hidden="true"><rect x="3" y="0.5" width="6" height="11" rx="1" fill="none" stroke="var(--white)" stroke-width="1.3"/><circle cx="6" cy="9.5" r="0.7" fill="var(--white)"/></svg>
        </li>
        <li class="contact__item">info@brightvale.com
          <svg class="contact__icon" viewBox="0 0 12 12" aria-hidden="true"><rect x="0.5" y="2.5" width="11" height="7.5" fill="var(--white)"/><path d="M0.5 2.5 L6 7 L11.5 2.5" fill="none" stroke="var(--navy)" stroke-width="1"/></svg>
        </li>
        <li class="contact__item">www.brightvale.com
          <svg class="contact__icon" viewBox="0 0 12 12" aria-hidden="true"><circle cx="6" cy="6" r="5.5" fill="var(--white)"/><path d="M3 4 Q5 3 6 5 Q5 7 7 8 M7 2 Q9 4 9 6" fill="none" stroke="var(--navy)" stroke-width="1"/></svg>
        </li>
      </ul>
    </div>
  </section>

  <section class="card card--back">
    <div class="wordmark">Brightvale Fluid<br>Systems</div>
    <div class="tagline">If there is magic in the planet, it is contained in water</div>
  </section>
</body>
</html>
```